Brightly Fen business card for handing simple contact information and generating service awareness

Utilizing the attached logo(s), generate a professional, but approachable, card conveying a sense of capability and integrity. Please only use one logo of the four attached; the different colors are all acceptable, but preference will be given to a design integrating a teal/turquoise logo,

I do not know where to put in the contact information or details?

Target Market(s)

Agriculture, Farming, Timber, Forestry, Construction, Crane Service

Industry/Entity Type

Contact Information for Business Card

Name, Phone Number, email address

Colors

Designer to choose colors to be used in the design.

Requirements
Nice to have
• It would be great to have either a mountain or one of the attached cranes as a backdrop on the rear of the card. Simple watermarks and/or Debossing is also great

```html
<!DOCTYPE html>
<html lang="en">
<head>
<meta charset="utf-8">
<title>Brightly Fen — Business Card</title>
<link href="https://fonts.googleapis.com/css2?family=Lato:wght@400;700;900&display=swap" rel="stylesheet">
<style>
  :root {
    --stage: #d8dbdb;
    --forest: #0f3d2f;
    --paper: #f3f2ee;
    --paper-ink: #114233;
    --emboss: #e9ebe8;
  }
  * { box-sizing: border-box; margin: 0; padding: 0; }
  html, body { width: 1200px; height: 929px; overflow: hidden; }
  body {
    background: var(--stage);
    font-family: "Lato", sans-serif;
    display: flex;
    flex-direction: column;
    align-items: center;
    justify-content: center;
    gap: 60px;
  }
  .card {
    width: 640px;
    height: 366px;
    position: relative;
    box-shadow: 0 10px 28px rgba(0,0,0,0.14);
  }

  /* Front face */
  .card-front { background: var(--paper); color: var(--paper-ink); }
  .card-front .frame {
    position: absolute;
    inset: 18px;
    border: 7px solid var(--forest);
  }
  .card-front .frame::after {
    content: "";
    position: absolute;
    inset: 5px;
    border: 1.5px solid var(--forest);
  }
  .identity {
    position: absolute;
    left: 70px;
    top: 130px;
    width: 250px;
    text-align: right;
  }
  .identity .person-name {
    font-weight: 900;
    font-size: 36px;
    letter-spacing: 0.5px;
    line-height: 1;
  }
  .identity .person-title {
    font-size: 15px;
    margin-top: 6px;
  }
  .divider {
    position: absolute;
    left: 345px;
    top: 110px;
    width: 1.5px;
    height: 150px;
    background: var(--forest);
  }
  .contact-list {
    position: absolute;
    left: 372px;
    top: 108px;
    list-style: none;
    font-size: 13.5px;
    line-height: 1.35;
  }
  .contact-list li {
    display: flex;
    align-items: flex-start;
    gap: 9px;
    margin-bottom: 2px;
  }
  .contact-list svg {
    width: 12px;
    height: 12px;
    flex: none;
    margin-top: 3px;
    fill: var(--forest);
  }

  /* Back face */
  .card-back {
    background: var(--forest);
    display: flex;
    align-items: center;
    justify-content: center;
    gap: 16px;
  }
  .card-back .mark-dot {
    width: 30px;
    height: 30px;
    border-radius: 50%;
    background: var(--emboss);
  }
  .card-back .brand-name {
    font-weight: 900;
    font-size: 46px;
    color: var(--emboss);
    text-transform: uppercase;
    letter-spacing: 1px;
  }
</style>
</head>
<body>

  <section class="card card-front" aria-label="Business card front">
    <div class="frame"></div>
    <div class="identity">
      <p class="person-name">EVAN HOLLIS</p>
      <p class="person-title">Founder &amp; CEO</p>
    </div>
    <div class="divider"></div>
    <ul class="contact-list">
      <li>
        <svg viewBox="0 0 12 12"><path d="M6 0a4 4 0 0 0-4 4c0 3 4 8 4 8s4-5 4-8a4 4 0 0 0-4-4zm0 5.6A1.6 1.6 0 1 1 6 2.4a1.6 1.6 0 0 1 0 3.2z"/></svg>
        <span>4870 Alder Ridge Road<br>Millbrook, CT 06199</span>
      </li>
      <li>
        <svg viewBox="0 0 12 12"><path d="M2.4 0.6l2 2-1 1.5c.8 1.7 2.1 3 3.8 3.8l1.5-1 2 2-1.3 2.2C5 10.8 1.2 7 0.4 1.9z"/></svg>
        <span>(555) 210-4471</span>
      </li>
      <li>
        <svg viewBox="0 0 12 12"><path d="M3 0h6a1 1 0 0 1 1 1v10a1 1 0 0 1-1 1H3a1 1 0 0 1-1-1V1a1 1 0 0 1 1-1zm.8 1.4v7.8h4.4V1.4zM6 9.8a.6.6 0 1 0 0 1.2.6.6 0 0 0 0-1.2z"/></svg>
        <span>(555) 210-4472</span>
      </li>
      <li>
        <svg viewBox="0 0 12 12"><path d="M3 0h6v3H3zM1 4h10a1 1 0 0 1 1 1v4H10v3H2V9H0V5a1 1 0 0 1 1-1zm2.2 4.4v2.4h5.6V8.4z"/></svg>
        <span>(555) 210-4473</span>
      </li>
      <li>
        <svg viewBox="0 0 12 12"><path d="M0 2h12v1L6 7 0 3zM0 4.4l6 4 6-4V10H0z"/></svg>
        <span>info@brightlyfen.com</span>
      </li>
      <li>
        <svg viewBox="0 0 12 12"><path d="M6 0a6 6 0 1 0 0 12A6 6 0 0 0 6 0zm0 1.2c.8 0 1.6 1.6 1.9 3.8H4.1C4.4 2.8 5.2 1.2 6 1.2zM1.3 6.2h2.6c.1 1.8.5 3.2 1 4.1A4.8 4.8 0 0 1 1.3 6.2zm6.8 4.1c.5-.9.9-2.3 1-4.1h2.6a4.8 4.8 0 0 1-3.6 4.1z"/></svg>
        <span>brightlyfen.com</span>
      </li>
    </ul>
  </section>

  <section class="card card-back" aria-label="Business card back">
    <span class="mark-dot"></span>
    <span class="brand-name">Brightly Fen</span>
  </section>

</body>
</html>
```